Website design for online service business

The company provides the following services:
1 - consultancy services on existing products (like tallydesk and brisk 354)
2 - Coaching services - Coach someone on services like using/developing features with existing products, or teach how to be more productive, or improve their business using automation, etc
3 - Training
- Online training on demand on existing products via vokra (like in Tallydesk and brisk 365)
- Online courses through videos lessons and scripts by offering information products where people will need to register and pay in advance to access the online course. (productivity courses for example)

- The goal is for clients to book time with me for one of those areas without too many clicks.
- Clients will be able to Book time using an integration (it would be good to have the layout integrated with the site.) with this https://planner.brisk-suite.example/owa/calendar/BrightKelpStudio1@brightkelpstudio.bookhub.example/bookings/

- there will be areas for which i whish to build a VIP mailing list. It's referenced on the wireframes

References:
https://www.lanternfieldnotes.example/about/about-dorvan/
https://www.pebblecompass.example/
https://tallydeskguide.example/

Target Market(s)

- Small businesses
- Freelancers

Industry/Entity Type

Business

Number of Pages Required

5+ page

Font styles to use
Sans Serif

Colors

Designer to choose colors to be used in the design.

Requirements
Must have
• Must have the design optimized to the less clicks possible to achieve any action
• The colors of the site should follow the logo (provided in attach)
• It should use other color that belong to the same pallet of colors
• Should contain colors that incentivizes people to click and book something
• Images and backgrounds should be made available
• All images sizes and colors should be provided to be able to develop the site according to the design
Nice to have
• The bookings for the time should be integrated within the design. If not possible a redirection to it can work as well.
Should not have
• Links to social media
• Pop-ups
• Intrusive navigations (like navigation bares on the left or right hand side)
• Should not be a template used by many people

```html
<!DOCTYPE html>
<html lang="en">
<head>
<meta charset="utf-8">
<title>Brightkelp Studio — Consulting, Coaching and Training</title>
<link rel="stylesheet" href="https://fonts.googleapis.com/css2?family=Poppins:wght@400;500;600;700&family=Montserrat:wght@400;500;600;700&display=swap">
<style>
:root{
  --orange:#f7861b;
  --navy:#1e4f86;
  --blue:#1b63ad;
  --blue-dark:#0e447f;
  --ink:#1f1f1f;
  --text:#333;
  --muted:#555;
  --panel:#d8e6ee;
  --footer:#f1f1f1;
  --white:#fff;
}
*{box-sizing:border-box;margin:0;padding:0}
html,body{width:1200px;height:3586px;overflow:hidden}
body{font-family:"Montserrat",sans-serif;color:var(--text);background:var(--white);position:relative}
.abs{position:absolute}
.btn{display:inline-block;background:var(--orange);color:var(--white);font-family:"Montserrat",sans-serif;font-weight:700;font-size:14px;text-transform:uppercase;text-decoration:none;text-align:center;border-radius:2px}
h1,h2,h3{font-family:"Poppins",sans-serif}

/* hero */
.hero{position:absolute;left:0;top:0;width:1200px;height:669px;overflow:hidden}
.hero-bg{position:absolute;inset:0;background:radial-gradient(circle at 880px 300px,#b8892a 0%,#4a4a3a 18%,#263040 40%,#161b24 75%,#0f1218 100%)}
.logo{position:absolute;display:flex;align-items:center;gap:10px;font-family:"Poppins",sans-serif;font-weight:600;letter-spacing:2px;text-transform:uppercase;line-height:1.1}
.logo .mark{width:22px;height:22px;background:var(--orange);flex:none}
.hero .logo{left:96px;top:50px;color:var(--white);font-size:22px}
.call{left:655px;top:32px;display:flex;align-items:center;gap:12px;color:var(--white)}
.call small{display:block;font-size:15px}
.call strong{display:block;font-size:19px;font-weight:500}
.search{left:882px;top:42px;width:218px;height:28px;background:var(--white);border-radius:14px;font-size:11px;color:#777;padding:7px 14px}
.search svg{position:absolute;right:12px;top:8px}
.nav{left:430px;top:102px;display:flex;gap:0;list-style:none}
.nav li{font-family:"Poppins",sans-serif;font-weight:600;font-size:17px;color:var(--white);text-transform:uppercase;margin-right:27px}
.nav li:last-child{margin-right:0}
.hero h1{left:96px;top:255px;color:var(--white);font-weight:700;font-size:52px;line-height:1;text-transform:uppercase}
.hero h1 span{display:block;font-size:36px;margin-top:10px}
.hero p{left:96px;top:380px;width:520px;color:var(--white);font-size:15px;line-height:1.7;font-weight:500}
.hero .btn{left:96px;top:455px;width:120px;height:34px;line-height:34px}
.dots{left:98px;top:521px;display:flex;gap:7px;align-items:center}
.dots i{display:block;width:10px;height:10px;border-radius:50%;background:var(--white)}
.dots i.on{width:16px;height:16px;border:2px solid var(--white);background:transparent;position:relative}
.dots i.on::after{content:"";position:absolute;left:3px;top:3px;width:6px;height:6px;border-radius:50%;background:var(--white)}

/* services */
.help{position:absolute;left:0;top:669px;width:1200px;height:660px}
.help h2{position:absolute;left:0;width:1200px;top:66px;text-align:center;font-size:35px;font-weight:600;color:var(--ink);line-height:1.3;text-transform:uppercase}
.help h2 span{display:block;color:var(--orange)}
.offer{position:absolute;top:210px;width:290px;text-align:center}
.offer .icon{width:150px;height:150px;margin:0 auto;background:var(--navy);border-radius:14px;position:relative}
.offer .icon::after{content:"";position:absolute;right:-6px;top:-8px;width:26px;height:26px;border-radius:50%;background:var(--orange)}
.offer h3{margin-top:36px;font-size:24px;font-weight:500;color:var(--ink)}
.offer p{margin-top:14px;font-size:13.5px;line-height:1.75;color:var(--text)}
.offer .btn{margin-top:24px;width:118px;height:34px;line-height:34px;font-size:13px}

/* why */
.why{position:absolute;left:0;top:1329px;width:1200px;height:456px;background:var(--panel)}
.why-photo{position:absolute;left:0;top:0;width:660px;height:456px;background:linear-gradient(100deg,#6f8aa0 0%,#9cb3c3 50%,#c9d9e2 100%)}
.why h2{position:absolute;left:663px;top:70px;font-size:35px;font-weight:600;line-height:1.15;color:var(--ink);text-transform:uppercase}
.why p{position:absolute;left:666px;top:170px;width:440px;font-size:13.5px;line-height:1.95;font-weight:500}
.why .btn{position:absolute;left:666px;top:350px;width:124px;height:36px;line-height:36px}

/* testimonial */
.quote{position:absolute;left:0;top:1785px;width:1200px;height:390px;background:linear-gradient(180deg,#1b1d22,#23262c 50%,#15171b);overflow:hidden}
.quote blockquote{position:absolute;left:220px;top:170px;width:760px;text-align:center;color:var(--white);font-size:19px;line-height:1.6}
.quote cite{position:absolute;left:0;width:1200px;top:282px;text-align:center;color:var(--white);font-size:15px;font-style:normal}
.quote .mark{position:absolute;left:561px;top:70px}
.arrow{position:absolute;top:203px}

/* blog */
.blog{position:absolute;left:0;top:2175px;width:1200px;height:602px}
.blog h2{position:absolute;left:0;width:1200px;top:83px;text-align:center;font-size:34px;font-weight:600;color:var(--ink);text-transform:uppercase}
.post{position:absolute;top:167px;width:310px}
.post .thumb{height:178px;background:linear-gradient(135deg,#5c6b78,#9aa6ae 60%,#d8dde0)}
.post h3{margin-top:18px;font-size:18px;font-weight:500;color:var(--ink)}
.meta{margin-top:12px;display:flex;gap:24px;font-size:11.5px;font-style:italic;color:var(--ink);align-items:center}
.meta span{display:flex;align-items:center;gap:6px}
.post p{margin-top:10px;font-size:12.5px;line-height:1.6}

/* call to action */
.cta{position:absolute;left:0;top:2777px;width:1200px;height:442px;background:linear-gradient(135deg,#2a74bd 0%,var(--blue) 45%,var(--blue-dark) 100%);color:var(--white);text-align:center}
.cta h2{position:absolute;left:0;width:1200px;top:90px;font-size:35px;font-weight:600;text-transform:uppercase}
.cta .lead{position:absolute;left:0;width:1200px;top:148px;font-size:21px}
.cta .body{position:absolute;left:220px;width:760px;top:192px;font-size:18px;line-height:1.6}
.cta .coffee{position:absolute;left:0;width:1200px;top:263px;font-size:21px}
.cta .btn{position:absolute;left:528px;top:310px;width:144px;height:40px;line-height:40px;font-size:15px}

/* footer */
.footer{position:absolute;left:0;top:3219px;width:1200px;height:304px;background:var(--footer)}
.footer .logo{left:96px;top:72px;color:var(--navy);font-size:20px}
.social{position:absolute;left:122px;top:188px;display:flex;gap:6px}
.social i{display:block;width:28px;height:28px;border:1.5px solid #444;border-radius:50%}
.footer h3{position:absolute;top:55px;font-size:19px;font-weight:600;color:var(--ink);text-transform:uppercase}
.news p{position:absolute;left:343px;top:99px;width:260px;font-size:12px;line-height:1.6}
.news .field{position:absolute;left:343px;top:152px;width:270px;height:38px;background:var(--white);border:1px solid #ccc;font-size:11px;color:#555;padding:12px 12px}
.news .btn{position:absolute;left:343px;top:204px;width:125px;height:32px;line-height:32px;font-size:12px}
.contact li{position:absolute;left:682px;display:flex;gap:12px;font-size:13px;line-height:1.6;list-style:none}
.links{position:absolute;left:972px;top:106px;list-style:none;font-size:12.5px;line-height:25px}
.copy{position:absolute;left:0;top:3523px;width:1200px;height:63px;border-top:1px solid #ddd;text-align:center;font-size:13px;padding-top:22px;color:var(--text)}
</style>
</head>
<body>

<header class="hero">
  <div class="hero-bg" role="img" aria-label="Hand holding a glowing city skyline with data search graphics on a dark background"></div>
  <div class="logo"><span class="mark"></span>Brightkelp<br>Studio</div>
  <div class="abs call">
    <svg width="36" height="36" viewBox="0 0 36 36" aria-hidden="true"><circle cx="18" cy="18" r="16" fill="none" stroke="#fff" stroke-width="2"/><path d="M12 10c1-1 2-1 3 0l2 3c.5 1 0 2-1 2.5-.5.3-.5 1 0 2l2 2.5c.8.8 1.5 1 2 .5.5-1 1.5-1.5 2.5-1l3 2c1 1 1 2 0 3-2 2-5 2-8-1l-4-4c-3-3-3.5-6.5-1.5-9.5z" fill="#fff"/></svg>
    <div><small>Call Us</small><strong>(08) 5550 2914</strong></div>
  </div>
  <div class="abs search">Search
    <svg width="11" height="11" viewBox="0 0 11 11" aria-hidden="true"><circle cx="4.5" cy="4.5" r="3.5" fill="none" stroke="#333" stroke-width="1.5"/><path d="M7 7l3 3" stroke="#333" stroke-width="1.5"/></svg>
  </div>
  <ul class="abs nav">
    <li>Home</li><li>About</li><li>Services</li><li>Training</li><li>Clients</li><li>Blog</li><li>Contact</li>
  </ul>
  <h1 class="abs">Because Ideas<span>Are a Million</span></h1>
  <p class="abs">Sed ut perspiciatis unde omnis iste natus voluptatem accusantium doloremque laudantium, totam rem aperiam</p>
  <a class="abs btn">Read More</a>
  <div class="abs dots"><i class="on"></i><i></i><i></i><i></i></div>
</header>

<section class="help">
  <h2>How can I help you with<span>your idea?</span></h2>
  <div class="offer" style="left:93px">
    <div class="icon" role="img" aria-label="Icon of a teacher presenting at a board"></div>
    <h3>I will teach you</h3>
    <p>I want to learn at my own pace. You teach me how things are done and how it works and I will do it myself.</p>
    <a class="btn">Teach me!</a>
  </div>
  <div class="offer" style="left:453px">
    <div class="icon" role="img" aria-label="Icon of a balloon and paper plane"></div>
    <h3>We do it together</h3>
    <p>I want to learn how it works and want to do it but I need someone that works along side with me to move forward and get it done.</p>
    <a class="btn">Let's do it!</a>
  </div>
  <div class="offer" style="left:810px">
    <div class="icon" role="img" aria-label="Icon of a person working at a desk"></div>
    <h3>I'll do it for you</h3>
    <p>I have this great idea but I just want to have it done for me. I don't want to do it or even learn about it.</p>
    <a class="btn">Do it for me!</a>
  </div>
</section>

<section class="why">
  <div class="why-photo" role="img" aria-label="Consultant in glasses working at a laptop while holding a phone"></div>
  <h2>Why should you<br>hire my services</h2>
  <p>Sed ut perspiciatis unde omnis iste natus error sit voluptatem accusantium doloremque laudantium, totam rem aperiam, eaque ipsa quae ab illo inventore veritatis et quasi architecto beatae vitae dicta sunt explicabo. Nemo enim ipsam voluptatem quia voluptas sit aspernatur aut odit aut fugit, sed quia consequuntur magni dolores</p>
  <a class="btn">Read More</a>
</section>

<section class="quote" role="img" aria-label="Dark photo of a team meeting around a table">
  <svg class="mark" width="78" height="64" viewBox="0 0 78 64" aria-hidden="true"><path d="M4 0h28v30c0 18-10 30-26 34l-2-8c9-3 13-10 13-18H4zM46 0h28v30c0 18-10 30-26 34l-2-8c9-3 13-10 13-18H46z" fill="#fff"/></svg>
  <svg class="arrow" style="left:122px" width="24" height="24" viewBox="0 0 24 24" aria-hidden="true"><path d="M22 2L2 12l20 10z" fill="#fff"/></svg>
  <svg class="arrow" style="left:1046px" width="24" height="24" viewBox="0 0 24 24" aria-hidden="true"><path d="M2 2l20 10L2 22z" fill="#fff"/></svg>
  <blockquote>Sed ut perspiciatis unde omnis iste natus error sit voluptatem accusantium doloremque laudantium, totam rem aperiam, eaque ipsa quae ab illo inventore veritatis et quasi architecto beatae vitae dicta sunt explicabo.</blockquote>
  <cite>- Rowan Tellis, Brightkelp Studio</cite>
</section>

<section class="blog">
  <h2>Latest Blog</h2>
  <article class="post" style="left:98px">
    <div class="thumb" role="img" aria-label="Business team discussing around a meeting table"></div>
    <h3>Nemo enim ipsam voluptatem</h3>
    <div class="meta"><span><svg width="11" height="11" viewBox="0 0 11 11" aria-hidden="true"><rect x="1" y="2" width="9" height="8" fill="none" stroke="#222"/><path d="M1 4h9" stroke="#222"/></svg>March 25, 2018</span><span><svg width="12" height="11" viewBox="0 0 12 11" aria-hidden="true"><path d="M1 1h10v6H5l-3 3V7H1z" fill="none" stroke="#222"/></svg>No comments</span></div>
    <p>Sed ut perspiciatis unde omnis iste natus error sit uptatem accusantium doloremque laudantium, totam rem aperiam, eaque ipsa</p>
  </article>
  <article class="post" style="left:445px">
    <div class="thumb" role="img" aria-label="Two people shaking hands over a desk"></div>
    <h3>Nemo enim ipsam voluptatem</h3>
    <div class="meta"><span><svg width="11" height="11" viewBox="0 0 11 11" aria-hidden="true"><rect x="1" y="2" width="9" height="8" fill="none" stroke="#222"/><path d="M1 4h9" stroke="#222"/></svg>March 25, 2018</span><span><svg width="12" height="11" viewBox="0 0 12 11" aria-hidden="true"><path d="M1 1h10v6H5l-3 3V7H1z" fill="none" stroke="#222"/></svg>No comments</span></div>
    <p>Sed ut perspiciatis unde omnis iste natus error sit uptatem accusantium doloremque laudantium, totam rem aperiam, eaque ipsa</p>
  </article>
  <article class="post" style="left:790px">
    <div class="thumb" role="img" aria-label="Team in a boardroom reviewing a chart on a screen"></div>
    <h3>Nemo enim ipsam voluptatem</h3>
    <div class="meta"><span><svg width="11" height="11" viewBox="0 0 11 11" aria-hidden="true"><rect x="1" y="2" width="9" height="8" fill="none" stroke="#222"/><path d="M1 4h9" stroke="#222"/></svg>March 25, 2018</span><span><svg width="12" height="11" viewBox="0 0 12 11" aria-hidden="true"><path d="M1 1h10v6H5l-3 3V7H1z" fill="none" stroke="#222"/></svg>No comments</span></div>
    <p>Sed ut perspiciatis unde omnis iste natus error sit uptatem accusantium doloremque laudantium, totam rem aperiam, eaque ipsa</p>
  </article>
</section>

<section class="cta">
  <h2>Don´t worry about anything.</h2>
  <p class="lead">I´m here for you !</p>
  <p class="body">Use the button bellow to book a time slot where we can have a chat about what you need help with and we will take it from there.</p>
  <p class="coffee">With coffee included of course!</p>
  <a class="btn">Book Me</a>
</section>

<footer class="footer">
  <div class="logo"><span class="mark"></span>Brightkelp<br>Studio</div>
  <div class="social"><i></i><i></i><i></i><i></i></div>

  <div class="news">
    <h3 style="left:343px">Sign up for newsletter</h3>
    <p>Excepteur sint occaecat cupidatat non proident, sunt in culpa qui officia deserunt</p>
    <div class="field">Enter email</div>
    <a class="btn">Subscription</a>
  </div>

  <ul class="contact">
    <h3 style="left:682px">Contact us</h3>
    <li style="top:100px"><svg width="13" height="16" viewBox="0 0 13 16" aria-hidden="true"><path d="M6.5 15S1 9 1 6a5.5 5.5 0 0111 0c0 3-5.5 9-5.5 9z" fill="var(--navy)"/><circle cx="6.5" cy="6" r="2" fill="#fff"/></svg><span>Brightkelp Studio 42, Fernwick,<br>Eastvale, EV4 2LP</span></li>
    <li style="top:163px"><svg width="13" height="14" viewBox="0 0 13 14" aria-hidden="true"><path d="M2 1c1-1 2-.5 2.5.5l1 2c.3 1-.5 1.5-1 2 0 1 2 3.5 3.5 4 .5-.5 1-1.3 2-1l2 1c1 .5 1.3 1.5.5 2.5-2 2-5 1-8-2S0 3 2 1z" fill="var(--navy)"/></svg><span>Phone:&nbsp; 075 5550 3187</span></li>
    <li style="top:196px"><svg width="14" height="11" viewBox="0 0 14 11" aria-hidden="true"><rect x="0.5" y="0.5" width="13" height="10" fill="var(--navy)"/><path d="M1 1l6 5 6-5" fill="none" stroke="#fff"/></svg><span>Email:&nbsp; info@brightkelpstudio.example</span></li>
  </ul>

  <h3 style="left:972px">Quick links</h3>
  <ul class="links">
    <li>Home</li><li>About</li><li>My services</li><li>Resources</li><li>Blog</li><li>Contact Us</li>
  </ul>
</footer>

<div class="copy">©2018 Brightkelp Studio , All Rights Reserved.</div>

</body>
</html>
```